Inpatient and outpatient services for people who have undergone urinary and faecal diversions.
Rory Talbrick
Clinical Nurse Consultant Stomal Therapy
C/o K7f Surgical Unit
Carrowby Hospital
Carrowby 2318
P: 0413 587 240
P: 9731 2086 Pager: 63158
AS: 9731 4402 Clear writing and colour as people who read this may have vision problems
Information transfer about contact details, position of clinic, what to bring on follow up appointmants.

Target Market(s)

patients and staff to contact

Industry/Entity Type

Medical

Contact Information for Business Card

As above in Project description. Can use both sides.

Font styles to use
Decorative

Requirements
Must have
• Clear easy to read writing as patients may have eyesight problems
Nice to have
• Catchy colour & design

```html
<!DOCTYPE html>
<html lang="en">
<head>
<meta charset="utf-8">
<title>Rory Talbrick – Business Card</title>
<link rel="stylesheet" href="https://fonts.googleapis.com/css2?family=Roboto:wght@400;700&display=swap">
<style>
  :root {
    --backdrop: #2b2b2d;
    --card: #1e1e1f;
    --ink: #f2f2f2;
    --accent: #3fb6c4;
    --faint: #3a3a3c;
  }
  * { margin: 0; padding: 0; box-sizing: border-box; }
  html, body {
    width: 900px; height: 1200px; overflow: hidden;
    background: var(--backdrop);
    font-family: "Roboto", Arial, sans-serif;
  }
  .sheet {
    width: 900px; height: 1200px;
    display: grid; grid-template-rows: 600px 600px;
    place-items: center;
  }
  .card {
    position: relative;
    width: 560px; height: 342px;
    background: var(--card);
    border-radius: 4px;
    box-shadow: 0 18px 40px rgba(0,0,0,0.45);
    overflow: hidden;
  }
  .card-front { display: grid; place-items: center; }
  .wordmark {
    color: var(--ink);
    font-weight: 400;
    font-size: 34px;
    letter-spacing: 0.04em;
  }
  .back-wordmark {
    position: absolute;
    right: -20px; bottom: 10px;
    color: var(--faint);
    font-weight: 700;
    font-size: 92px;
    line-height: 0.9;
    text-align: right;
    white-space: nowrap;
  }
  .contact {
    position: absolute;
    left: 44px; top: 52px;
    color: var(--ink);
    font-size: 17px;
    line-height: 1.32;
  }
  .contact-name {
    font-weight: 700;
    font-size: 19px;
    text-transform: uppercase;
    letter-spacing: 0.02em;
  }
  .contact-role { color: var(--accent); margin-bottom: 6px; }
  .contact-address { margin-bottom: 6px; }
  .label { color: var(--accent); }
</style>
</head>
<body>
  <main class="sheet">
    <section class="card card-front" aria-label="Card front">
      <span class="wordmark">Rory Talbrick</span>
    </section>

    <section class="card card-back" aria-label="Card back">
      <span class="back-wordmark" aria-hidden="true">Rory<br>Talbrick</span>
      <div class="contact">
        <p class="contact-name">Rory Talbrick</p>
        <p class="contact-role">Clinical Nurse Consultant Stomal Therapy</p>
        <div class="contact-address">
          <p>C/o K7f Surgical Unit</p>
          <p>Carrowby Hospital</p>
          <p>Carrowby 2318</p>
        </div>
        <p><span class="label">P:</span> 0413 587 240</p>
        <p><span class="label">P:</span> 9731 2086</p>
        <p><span class="label">Pager:</span> 63158</p>
        <p><span class="label">AS:</span> 9731 4402</p>
      </div>
    </section>
  </main>
</body>
</html>
```